LAMBERTINE KOVAX Vaporizer Company Thoughtful Kovax for a brighter daily path.

I need a logo design for a new Colorado based company. We wholesale exclusive vaporizer units. Smoke inhalation delivers damaging carcinogens and an onslaught of other damaging materials directly through the bronchial tree and into the lungs.What this means in more simple terms is that the vaporizer completely eliminates every last chemical that is directly associated with burning of the material.

It Company

```html
<!DOCTYPE html>
<html lang="en">
<head>
<meta charset="utf-8">
<title>Lambertine Kovax – Business Cards</title>
<link href="https://fonts.googleapis.com/css2?family=Bebas+Neue&family=Open+Sans:wght@400;500&display=swap" rel="stylesheet">
<style>
  :root {
    --backdrop: #d6d6d6;
    --card-dark: #3a3a3a;
    --card-light: #ffffff;
    --ink-light: #ffffff;
    --ink-muted: #8a8a8a;
    --ink-dark: #1c1c1c;
    --ink-brand: #3d3d3d;
    --rule: #a9a9a9;
    --brand-accent: #7fc2cb;
  }
  * { margin: 0; padding: 0; box-sizing: border-box; }
  html, body {
    width: 1200px;
    height: 883px;
    overflow: hidden;
    background: var(--backdrop);
  }
  .canvas {
    position: relative;
    width: 1200px;
    height: 883px;
  }
  .card {
    position: absolute;
    width: 342px;
    height: 220px;
  }
  .card--front {
    left: 487px;
    top: 180px;
    background: var(--card-dark);
  }
  .card--back {
    left: 485px;
    top: 487px;
    background: var(--card-light);
    text-align: center;
  }
  .brand-mark {
    position: absolute;
    border-radius: 50%;
    background: var(--brand-accent);
  }
  .card--front .brand-mark {
    left: 133px;
    top: 48px;
    width: 80px;
    height: 80px;
  }
  .card--back .brand-mark {
    left: 155px;
    top: 22px;
    width: 44px;
    height: 44px;
  }
  .brand-lockup {
    position: absolute;
    left: 6px;
    right: 0;
    top: 138px;
    text-align: center;
  }
  .brand-lockup__inner {
    display: inline-block;
    text-align: right;
  }
  .brand-name {
    display: block;
    font-family: "Bebas Neue", "Arial Narrow", sans-serif;
    font-size: 27px;
    line-height: 1;
    letter-spacing: 0.4px;
    color: var(--ink-light);
    white-space: nowrap;
  }
  .brand-tagline {
    display: block;
    margin-top: 1px;
    padding-right: 12px;
    font-family: "Bebas Neue", "Arial Narrow", sans-serif;
    font-size: 11px;
    line-height: 1;
    letter-spacing: 0.3px;
    color: var(--ink-muted);
    white-space: nowrap;
  }
  .brand-divider {
    position: absolute;
    left: 7px;
    right: 0;
    top: 73px;
    display: flex;
    align-items: center;
    gap: 10px;
  }
  .brand-divider::before,
  .brand-divider::after {
    content: "";
    flex: 1;
    height: 1px;
    background: var(--rule);
  }
  .brand-divider__name {
    font-family: "Bebas Neue", "Arial Narrow", sans-serif;
    font-size: 13px;
    line-height: 1;
    letter-spacing: 0.4px;
    color: var(--ink-brand);
  }
  .holder-name {
    position: absolute;
    left: 0; right: 0;
    top: 109px;
    font-family: "Open Sans", Arial, sans-serif;
    font-size: 16px;
    color: var(--ink-dark);
  }
  .holder-role {
    position: absolute;
    left: 0; right: 0;
    top: 130px;
    font-family: "Open Sans", Arial, sans-serif;
    font-size: 9.5px;
    color: var(--ink-dark);
  }
  .contact {
    position: absolute;
    left: 0; right: 0;
    top: 177px;
    font-family: "Open Sans", Arial, sans-serif;
    font-size: 9.5px;
    line-height: 15px;
    color: var(--ink-dark);
  }
</style>
</head>
<body>
  <main class="canvas">
    <section class="card card--front" aria-label="Card front">
      <span class="brand-mark" aria-hidden="true"></span>
      <div class="brand-lockup">
        <div class="brand-lockup__inner">
          <span class="brand-name">LAMBERTINE KOVAX</span>
          <span class="brand-tagline">VAPORIZER COMPANY</span>
        </div>
      </div>
    </section>

    <section class="card card--back" aria-label="Card back">
      <span class="brand-mark" aria-hidden="true"></span>
      <div class="brand-divider">
        <span class="brand-divider__name">LAMBERTINE KOVAX</span>
      </div>
      <p class="holder-name">Dorian Pelleck</p>
      <p class="holder-role">Manager</p>
      <p class="contact">
        418 Quarry Bend Road, Alder Falls, CO 80517<br>
        Phone: +1 555 014 22 90
      </p>
    </section>
  </main>
</body>
</html>
```